Halvorsen Partners Business Card

Halvorsen Partners Civil Construction
Marcus Halvorsen
CEO
727-518-6094
Marcus@HalvorsenSiteworks.example
www.HalvorsenSiteworks.example
Site Development
Utility Construction
Excavation
40876 County Lane 19
Brookhaven, FL 34990

Target Market(s)

Construction and government

Industry/Entity Type

Business

Contact Information for Business Card

I want an unique design that make a statement

Number of Pages Required

1 page

Font styles to use

Colors

Designer to choose colors to be used in the design.

Requirements
Must have
• unique design, feel free to modify or change the color of my logo.
Nice to have
• extra design features like spot UV, foil accents, color edges, unique paper, or any thing that would make my card pop.
• I like the feel of the image that I attached

```html
<!DOCTYPE html>
<html lang="en">
<head>
<meta charset="utf-8">
<title>Halvorsen Partners Business Card</title>
<link href="https://fonts.googleapis.com/css2?family=Lato:wght@400;700&family=PT+Sans+Narrow:wght@400;700&display=swap" rel="stylesheet">
<style>
  :root {
    --bg: #6b6d70;
    --navy: #2e4a8c;
    --ink: #2b2b2b;
    --paper: #ffffff;
    --paper-shade: #eef0f4;
    --sky-top: #8c98ad;
    --sky-mid: #4e5a70;
    --ground: #0d0f14;
    --white: #ffffff;
  }
  * { margin: 0; padding: 0; box-sizing: border-box; }
  html, body { width: 1200px; height: 907px; overflow: hidden; }
  body {
    background: var(--bg);
    font-family: "PT Sans Narrow", "Arial Narrow", sans-serif;
    display: flex;
    align-items: center;
    justify-content: center;
    gap: 40px;
  }
  .card {
    position: relative;
    width: 540px;
    height: 309px;
    border-radius: 6px;
    overflow: hidden;
    box-shadow: 0 10px 24px rgba(0,0,0,0.35);
  }

  /* Front */
  .card-front { background: var(--ground); }
  .front-photo {
    position: absolute; inset: 0;
    background: linear-gradient(160deg, var(--sky-top) 0%, var(--sky-mid) 45%, #20252f 70%, var(--ground) 100%);
  }
  .front-brand {
    position: absolute;
    left: 130px; top: 112px;
    display: flex; align-items: center; gap: 14px;
  }
  .brand-mark {
    width: 14px; height: 14px;
    flex: none;
    background: var(--white);
  }
  .front-name {
    font-family: "Lato", sans-serif;
    font-weight: 400;
    color: var(--white);
    font-size: 22px;
    line-height: 1.15;
    letter-spacing: 0.06em;
    text-transform: uppercase;
  }
  .front-web {
    position: absolute;
    left: 158px; top: 188px;
    color: var(--white);
    font-size: 15px;
    letter-spacing: 0.1em;
  }

  /* Back */
  .card-back { background: var(--paper); }
  .back-shade {
    position: absolute; right: 0; top: 0; bottom: 0;
    width: 150px;
    background: var(--paper-shade);
  }
  .name-tab {
    position: absolute;
    right: 150px; top: 0;
    width: 200px; height: 54px;
    background: var(--navy);
    border-radius: 0 0 6px 6px;
    color: var(--white);
    display: flex; align-items: center; justify-content: center; gap: 10px;
  }
  .person-name { font-family: "Lato", sans-serif; font-weight: 700; font-size: 17px; }
  .person-title { font-size: 11px; opacity: 0.85; }
  .back-brand {
    position: absolute; left: 30px; top: 76px;
    display: flex; align-items: center; gap: 12px;
  }
  .back-brand .brand-mark { background: var(--navy); }
  .back-name {
    font-family: "Lato", sans-serif;
    font-weight: 400;
    color: var(--navy);
    font-size: 19px;
    line-height: 1.15;
    letter-spacing: 0.05em;
    text-transform: uppercase;
  }
  .contact-list {
    position: absolute; left: 30px; top: 140px;
    list-style: none;
    color: var(--ink);
    font-size: 15px;
    line-height: 1.25;
  }
  .contact-list li { display: flex; align-items: flex-start; gap: 10px; margin-bottom: 6px; }
  .contact-list svg { width: 12px; height: 12px; margin-top: 3px; fill: var(--navy); flex: none; }
  .service-band {
    position: absolute; left: 0; right: 0; bottom: 0;
    height: 30px;
    background: var(--navy);
    color: var(--white);
    font-size: 12px;
    font-weight: 700;
    letter-spacing: 0.12em;
    text-transform: uppercase;
    display: flex; align-items: center; justify-content: center;
  }
  .service-band span + span::before { content: "-"; margin: 0 8px; }
</style>
</head>
<body>
  <div class="card card-front">
    <div class="front-photo" role="img" aria-label="Dusk photograph of an excavator and construction machinery silhouetted against a blue-grey sky"></div>
    <div class="front-brand">
      <div class="brand-mark"></div>
      <div class="front-name">Halvorsen Partners<br>Civil Construction</div>
    </div>
    <div class="front-web">www.HalvorsenSiteworks.example</div>
  </div>

  <div class="card card-back">
    <div class="back-shade"></div>
    <div class="name-tab">
      <span class="person-name">Marcus Halvorsen</span>
      <span class="person-title">CEO</span>
    </div>
    <div class="back-brand">
      <div class="brand-mark"></div>
      <div class="back-name">Halvorsen Partners<br>Civil Construction</div>
    </div>
    <ul class="contact-list">
      <li>
        <svg viewBox="0 0 12 12"><path d="M6 0a4 4 0 0 0-4 4c0 3 4 8 4 8s4-5 4-8a4 4 0 0 0-4-4zm0 5.5A1.5 1.5 0 1 1 6 2.5a1.5 1.5 0 0 1 0 3z"/></svg>
        <span>40876 County Lane 19<br>Brookhaven, FL 34990</span>
      </li>
      <li>
        <svg viewBox="0 0 12 12"><path d="M2.5 0.5l2 2.5-1.2 1.4a7 7 0 0 0 4.3 4.3L9 7.5l2.5 2-1.3 2C5 11.5 0.5 7 0.5 1.8z"/></svg>
        <span>727-518-6094</span>
      </li>
      <li>
        <svg viewBox="0 0 12 12"><path d="M0 2h12v8H0zM0.8 2.6L6 6.6l5.2-4v0.9L6 7.6 0.8 3.5z" fill-rule="evenodd"/></svg>
        <span>Marcus@HalvorsenSiteworks.example</span>
      </li>
      <li>
        <svg viewBox="0 0 12 12"><circle cx="6" cy="6" r="5.5"/></svg>
        <span>www.HalvorsenSiteworks.example</span>
      </li>
    </ul>
    <div class="service-band">
      <span>Site Development</span><span>Utility Construction</span><span>Excavation</span>
    </div>
  </div>
</body>
</html>
```